Classy, Elegant, Simple Business Card Design

Looking to have a classy, simple, and elegant design. Want a top notch designed business card. I really like the look of the new brivo credit card. I also like the design I attached. I am trying to reach 21-29 year old females for booking us for there wedding or event. We offer Disc Jockey Service, Photo Booth Rentals, and Uplighting .

Target Market(s)

21-28 year old females

Contact Information for Business Card

Has to have logo, website, email, and phone number

Font styles to use
Other font styles liked:
• open to font choice, modern, clean
Designer to choose
33a6d7
0791cd
0555a3
ffffff

Requirements
Must have
• Has to have logo, website, email, and phone number
Nice to have
• I really like the design of the new brivo credit card. I also included my logo and some designs I like
Should not have
• clutter or too much info

```html
<!DOCTYPE html>
<html lang="en">
<head>
<meta charset="utf-8">
<title>Tidelight Event Group – Business Card</title>
<link rel="stylesheet" href="https://fonts.googleapis.com/css2?family=Questrial&family=Roboto:wght@400;700&display=swap">
<style>
  :root {
    --stage: #3a3b3e;
    --card-dark: #1d1e21;
    --sky: #33a6d7;
    --azure: #0791cd;
    --navy: #0555a3;
    --white: #ffffff;
    --mist: #c9d6e2;
  }
  * { box-sizing: border-box; margin: 0; padding: 0; }
  html, body { width: 799px; height: 1200px; overflow: hidden; }
  body {
    background: var(--stage);
    position: relative;
    font-family: "Roboto", sans-serif;
  }
  .card {
    position: absolute;
    left: 80px;
    width: 640px;
    height: 366px;
    border-radius: 4px;
    overflow: hidden;
    background: var(--card-dark);
    box-shadow: 0 14px 30px rgba(0,0,0,.45);
  }
  .card--front { top: 156px; }
  .card--back { top: 678px; }

  /* front */
  .front-brand {
    position: absolute;
    top: 108px;
    left: 0;
    width: 100%;
    display: flex;
    align-items: center;
    justify-content: center;
    gap: 14px;
  }
  .brand-dot {
    width: 16px; height: 16px;
    border-radius: 50%;
    background: var(--azure);
  }
  .brand-name {
    font-family: "Questrial", sans-serif;
    font-weight: 400;
    color: var(--azure);
    letter-spacing: 3px;
    text-transform: uppercase;
    white-space: nowrap;
  }
  .front-brand .brand-name { font-size: 32px; }
  .sound-band {
    position: absolute;
    left: 0; right: 0; bottom: 0;
    height: 110px;
    background: linear-gradient(to top, rgba(7,145,205,.85), rgba(51,166,215,.15) 80%, rgba(51,166,215,0));
  }

  /* back */
  .back-header {
    position: absolute;
    top: 0; left: 0; right: 0;
    height: 118px;
    display: flex;
    align-items: center;
    padding-left: 60px;
    gap: 14px;
  }
  .back-header .brand-name { font-size: 28px; }
  .back-panel {
    position: absolute;
    top: 118px; left: 0; right: 0; bottom: 0;
    background: linear-gradient(90deg, var(--navy) 0%, #0a68b4 60%, var(--azure) 100%);
  }
  .holder {
    position: absolute;
    top: 28px; left: 40px;
    color: var(--white);
  }
  .holder-name { font-size: 26px; font-weight: 700; }
  .holder-role { font-size: 15px; margin-top: 2px; }
  .contact-list {
    list-style: none;
    margin-top: 18px;
    font-size: 15px;
  }
  .contact-list li {
    display: flex;
    align-items: center;
    gap: 12px;
    margin-bottom: 8px;
  }
  .contact-icon { width: 14px; height: 14px; flex: none; }
  .panel-mark {
    position: absolute;
    right: 40px; bottom: 40px;
    font-family: "Questrial", sans-serif;
    font-size: 52px;
    color: var(--sky);
    opacity: .45;
    letter-spacing: 3px;
    text-transform: uppercase;
  }
</style>
</head>
<body>

  <section class="card card--front">
    <div class="front-brand">
      <span class="brand-dot"></span>
      <span class="brand-name">Tidelight Event Group</span>
    </div>
    <div class="sound-band" role="img" aria-label="Blue audio equalizer bars rising across the bottom edge"></div>
  </section>

  <section class="card card--back">
    <header class="back-header">
      <span class="brand-dot"></span>
      <span class="brand-name">Tidelight Event Group</span>
    </header>
    <div class="back-panel">
      <div class="holder">
        <p class="holder-name">Evan Marlow</p>
        <p class="holder-role">Founder &amp; CEO</p>
        <ul class="contact-list">
          <li>
            <svg class="contact-icon" viewBox="0 0 16 16" aria-hidden="true"><path fill="#fff" d="M3.5 1h2.5l1.2 3.5-1.8 1.3a9 9 0 0 0 4.8 4.8l1.3-1.8 3.5 1.2v2.5A1.5 1.5 0 0 1 13.5 14 11.5 11.5 0 0 1 2 2.5 1.5 1.5 0 0 1 3.5 1z"/></svg>
            <span>555 0142 0187</span>
          </li>
          <li>
            <svg class="contact-icon" viewBox="0 0 16 16" aria-hidden="true"><rect x="1" y="3" width="14" height="10" fill="#fff"/><path d="M1 3l7 6 7-6" stroke="#0555a3" stroke-width="1.4" fill="none"/></svg>
            <span>evan@tidelightevents.com</span>
          </li>
          <li>
            <svg class="contact-icon" viewBox="0 0 16 16" aria-hidden="true"><circle cx="8" cy="8" r="6.5" fill="none" stroke="#fff" stroke-width="1.4"/><ellipse cx="8" cy="8" rx="2.8" ry="6.5" fill="none" stroke="#fff" stroke-width="1.2"/><path d="M1.5 8h13" stroke="#fff" stroke-width="1.2"/></svg>
            <span>www.tidelightevents.com</span>
          </li>
        </ul>
      </div>
      <span class="panel-mark">Tidelight</span>
    </div>
  </section>

</body>
</html>
```